Meridian Rest Supply Needs Business Card

Looking for a very nice looking business card. Creative but not extravagant. We sell beds and pillows across the U.S. and need something professional but catchy. I have attached the logo.

Name : Dale Fenwick
Title : President
Phone : (800) 417-2964
Email: sleep@quorvana.com
Website: www.quorvana.com

Can be single-sided or double-sided
horizontal or vertical

Can use Blues/Greys

Target Market(s)

Mass Market

Industry/Entity Type

Retail

Contact Information for Business Card

Name : Dale Fenwick
Title : President
Phone : (800) 417-2964
Email: sleep@quorvana.com
Website: www.quorvana.com

Requirements
Must have
• Clean, Modern, Smooth
• Can use Blues/Greys
• On the other side without the information - have something simple like www.quorvana.com or our logo
Nice to have
• Surprise me
Should not have
• Nothing crazy, nothing cluttered

```html
<!DOCTYPE html>
<html lang="en">
<head>
<meta charset="utf-8">
<title>Meridian Rest Supply – Business Card</title>
<link href="https://fonts.googleapis.com/css2?family=Open+Sans:wght@300;400;700&display=swap" rel="stylesheet">
<style>
  :root {
    --backdrop: #e4e5e7;
    --card-black: #000000;
    --brand-blue: #2ea6db;
    --logo-blue: #29a8e0;
    --ink-white: #ffffff;
    --card-w: 532px;
    --card-h: 304px;
  }
  * { box-sizing: border-box; margin: 0; padding: 0; }
  html, body {
    width: 1200px;
    height: 800px;
    overflow: hidden;
    background: var(--backdrop);
    font-family: "Open Sans", Arial, sans-serif;
  }
  .canvas {
    width: 1200px;
    height: 800px;
    display: flex;
    align-items: center;
    justify-content: center;
    gap: 48px;
  }
  .card {
    position: relative;
    width: var(--card-w);
    height: var(--card-h);
    background: var(--card-black);
    overflow: hidden;
    box-shadow: 0 10px 28px rgba(0, 0, 0, 0.18);
  }

  /* Back side: wordmark only */
  .card-back {
    display: flex;
    align-items: center;
    justify-content: center;
  }
  .wordmark {
    font-family: "Open Sans", Arial, sans-serif;
    font-weight: 300;
    letter-spacing: 2px;
    line-height: 1;
  }
  .card-back .wordmark {
    color: var(--logo-blue);
    font-size: 50px;
  }

  /* Front side: name panel + blue info band */
  .holder {
    position: absolute;
    top: 34px;
    left: 30px;
    color: var(--ink-white);
  }
  .holder-name {
    font-weight: 700;
    font-size: 17px;
    line-height: 1.1;
  }
  .holder-title {
    font-weight: 400;
    font-size: 11px;
    margin-top: 2px;
  }
  .info-band {
    position: absolute;
    top: 0;
    left: 190px;
    width: 258px;
    height: 100%;
    background: var(--brand-blue);
    color: var(--ink-white);
    padding: 66px 0 0 40px;
  }
  .info-band .wordmark {
    font-size: 38px;
    color: var(--ink-white);
  }
  .contact-list {
    list-style: none;
    margin-top: 38px;
  }
  .contact-item {
    display: flex;
    align-items: center;
    gap: 12px;
    font-size: 12px;
    font-weight: 400;
    height: 26px;
  }
  .contact-icon {
    width: 13px;
    height: 13px;
    flex: none;
  }
</style>
</head>
<body>
<main class="canvas">

  <section class="card card-back" aria-label="Card back">
    <span class="wordmark">quorvana</span>
  </section>

  <section class="card card-front" aria-label="Card front">
    <div class="holder">
      <p class="holder-name">Dale Fenwick</p>
      <p class="holder-title">President</p>
    </div>

    <div class="info-band">
      <span class="wordmark">quorvana</span>
      <ul class="contact-list">
        <li class="contact-item">
          <svg class="contact-icon" viewBox="0 0 24 24" aria-hidden="true">
            <path fill="#fff" d="M6.6 10.8c1.4 2.8 3.8 5.1 6.6 6.6l2.2-2.2c.3-.3.7-.4 1-.2 1.1.4 2.3.6 3.6.6.6 0 1 .4 1 1V20c0 .6-.4 1-1 1C10.6 21 3 13.4 3 4c0-.6.4-1 1-1h3.5c.6 0 1 .4 1 1 0 1.3.2 2.5.6 3.6.1.3 0 .7-.2 1L6.6 10.8z"/>
          </svg>
          <span>(800) 417-2964</span>
        </li>
        <li class="contact-item">
          <svg class="contact-icon" viewBox="0 0 24 24" aria-hidden="true">
            <g fill="none" stroke="#fff" stroke-width="2.4" stroke-linecap="round">
              <path d="M2 9a14 14 0 0 1 20 0"/>
              <path d="M5.5 12.5a9 9 0 0 1 13 0"/>
              <path d="M9 16a4 4 0 0 1 6 0"/>
            </g>
            <circle cx="12" cy="19.5" r="1.8" fill="#fff"/>
          </svg>
          <span>www.quorvana.com</span>
        </li>
        <li class="contact-item">
          <svg class="contact-icon" viewBox="0 0 24 24" aria-hidden="true">
            <rect x="2" y="5" width="20" height="14" rx="1.5" fill="#fff"/>
            <path d="M3 6.5l9 6.5 9-6.5" fill="none" stroke="#2ea6db" stroke-width="1.6"/>
          </svg>
          <span>sleep@quorvana.com</span>
        </li>
      </ul>
    </div>
  </section>

</main>
</body>
</html>
```